Website Design Required For Education Video Portfolio Site

I am looking for a designer to create a skin for a relaunch of my website - www.brightlarkfilms.co.uk. We want a clean and stylish new design.

The website showcases prospectus/promotional videos that are made for schools and colleges. Videos will be hosted on online video and embedded.

I want it to be stylish and clean.

I require 7 pages designed and this must be agreed in order to do the project.

1. Homepage
2. About
3. Prices
4. Testimonials
5. Contact Page with form
6. Promotional Videos
7. Subject Videos

The website will be then be built on the Wordpress system.

Target Market(s)

Education, Schools, Colleges, Universities

Industry/Entity Type

Education

Font styles to use
Serif

Colors

Designer to choose colors to be used in the design.

Requirements
Must have
• Video content, be clean, show our portfolio, descriptions about videos. I like the idea of having video headers.
Nice to have
• Images

```html
<!DOCTYPE html>
<html lang="en">
<head>
<meta charset="utf-8">
<title>Brightlark Films – Educational Videos</title>
<link href="https://fonts.googleapis.com/css2?family=Raleway:wght@600;700;800&family=Roboto:wght@400;500;700&display=swap" rel="stylesheet">
<style>
:root{
  --blue:#1ea7e8;
  --blue-dark:#0f86c9;
  --ink:#1b1b1b;
  --text:#666;
  --grey:#f3f3f3;
  --dark:#222;
  --white:#fff;
}
*{box-sizing:border-box;margin:0;padding:0}
html,body{width:1200px;height:5141px;overflow:hidden;background:var(--white)}
body{font-family:'Roboto',sans-serif;color:var(--text);position:relative}
h1,h2,h3,h4{font-family:'Raleway',sans-serif;color:var(--ink);text-transform:uppercase}
.section{position:absolute;left:0;width:1200px}
.rule{display:block;width:64px;height:4px;background:var(--blue);margin:14px auto 0}
.btn{display:inline-block;background:var(--blue);color:#fff;font:700 13px 'Roboto',sans-serif;text-transform:uppercase;padding:16px 22px;border-radius:4px;letter-spacing:.3px}
.photo{position:absolute}
/* header */
.header{top:0;height:110px}
.brand{position:absolute;left:110px;top:28px;display:flex;align-items:center;gap:12px}
.brand-mark{width:46px;height:46px;border-radius:50%;background:var(--blue)}
.brand-name{font:800 34px 'Raleway',sans-serif;color:var(--blue)}
.social{position:absolute;left:760px;top:38px;display:flex;gap:12px}
.social span{width:34px;height:34px;border-radius:50%;background:#fff;box-shadow:0 2px 8px rgba(0,0,0,.18)}
.phone-tab{position:absolute;right:0;top:0;width:300px;height:110px;background:var(--blue);clip-path:polygon(20% 0,100% 0,100% 100%,0 100%);color:#fff;font:700 24px 'Roboto',sans-serif;display:flex;align-items:center;justify-content:flex-end;padding-right:32px}
.nav{top:110px;height:50px;background:#000;display:flex;justify-content:center;align-items:center;gap:46px}
.nav a{color:#fff;font:700 12px 'Roboto',sans-serif;text-transform:uppercase;text-decoration:none}
.nav a.active{color:var(--blue)}
/* hero */
.hero{top:160px;height:600px;background:linear-gradient(135deg,#5a6a55,#2f7a5e 40%,#b0403c 60%,#6a5b4c)}
.hero-content{position:absolute;top:206px;width:100%;text-align:center}
.hero h1{color:#fff;font-size:42px;line-height:52px}
.hero .btn{margin-top:28px;padding:14px 22px}
/* intro */
.intro{top:760px;height:720px;text-align:center}
.intro h2{margin-top:100px;font-size:27px;line-height:40px}
.lead{font-size:13.5px;line-height:26px;width:950px;margin:26px auto 0}
.thumbs{position:absolute;left:114px;display:flex;gap:38px}
.thumb{width:300px;height:216px;position:relative;border:5px solid #fff;box-shadow:0 6px 18px rgba(0,0,0,.18)}
.thumb svg{position:absolute;left:50%;top:50%;transform:translate(-50%,-50%)}
/* investment */
.invest{top:1480px;height:700px}
.frame-top{position:absolute;left:644px;top:56px;width:278px;height:36px;border-top:3px solid var(--blue);border-right:3px solid var(--blue)}
.frame-bottom{position:absolute;left:278px;top:580px;width:282px;height:38px;border-left:3px solid var(--blue);border-bottom:3px solid var(--blue)}
.invest-panel{position:absolute;left:558px;top:90px;width:642px;height:570px;background:var(--grey);padding:68px 76px}
.invest-panel h2{font-size:29px;line-height:40px;text-align:left}
.invest-panel .rule{margin:10px 0 0}
.invest-panel p{font-size:13.5px;line-height:26px;margin-top:22px}
.invest-panel b{color:var(--ink)}
.invest-panel .btn{margin-top:28px}
/* partners */
.partners{top:2180px;height:400px;text-align:center}
.partners h2{margin-top:56px;font-size:28px;line-height:40px}
.logo-row{position:absolute;top:196px;left:112px;display:flex;gap:26px}
.logo-box{width:174px;height:90px;background:#fff;box-shadow:0 4px 14px rgba(0,0,0,.14);display:flex;align-items:center;justify-content:center}
.arrow-l{position:absolute;left:40px;top:228px}
.arrow-r{position:absolute;left:1130px;top:224px;width:34px;height:34px;border-radius:50%;background:var(--blue);display:flex;align-items:center;justify-content:center}
/* why */
.why{top:2580px;height:594px;background:linear-gradient(135deg,#1d9ee0,#1aa8ec 50%,#0f8fd6);text-align:center}
.why h2{color:#fff;font-size:33px;margin-top:72px}
.why .rule{background:#fff}
.cards{position:absolute;top:170px;left:112px;display:flex;gap:18px}
.card{width:314px;height:344px;background:#fff;border-radius:26px 26px 0 26px;padding:34px 26px}
.card-icon{width:88px;height:88px;border-radius:50%;background:#222;margin:0 auto;display:flex;align-items:center;justify-content:center}
.card-icon.alt{background:var(--blue)}
.card h3{font-size:15px;margin-top:32px}
.card p{font-size:12.5px;line-height:23px;margin-top:20px}
/* custom */
.custom{top:3174px;height:710px;text-align:center}
.custom h2{margin-top:110px;font-size:28px;line-height:40px}
.custom .lead b{color:var(--ink);font-weight:500}
.custom a{display:block;margin-top:16px;color:var(--blue);font-size:17px;text-decoration:underline}
/* budget */
.budget{top:3884px;height:472px;background:var(--grey)}
.budget-text{position:absolute;left:112px;top:92px;width:440px}
.budget h2{font-size:30px;line-height:40px}
.budget .rule{margin:12px 0 0}
.budget p{font-size:13.5px;line-height:26px;margin-top:26px}
.budget .btn{margin-top:26px}
/* aviation */
.aviation{top:4356px;height:404px;background:var(--dark);text-align:center}
.aviation h2{color:#fff;font-size:32px;line-height:40px;margin-top:104px}
.aviation p{color:#fff;font-size:18px;font-weight:500;margin-top:30px}
.aviation .btn{margin-top:26px}
/* footer */
.footer{top:4760px;height:381px}
.footer-brand{position:absolute;left:110px;top:148px;display:flex;align-items:center;gap:10px}
.footer-brand .brand-mark{width:40px;height:40px}
.footer-brand .brand-name{font-size:30px}
.col{position:absolute;top:74px}
.col h4{font:700 15px 'Roboto',sans-serif;color:var(--ink);text-transform:uppercase}
.col h4::after{content:"";display:block;width:40px;height:3px;background:var(--blue);margin-top:6px}
.col ul{list-style:none;margin-top:14px}
.col li{font-size:13px;line-height:28px;color:#555}
.contact-item{display:flex;gap:14px;font-size:13px;line-height:21px;color:#555;margin-top:14px;width:290px}
.email-field{width:226px;height:44px;border:1px solid #e2e2e2;box-shadow:0 2px 6px rgba(0,0,0,.08);font-size:13px;color:#777;padding:13px 16px;margin-top:20px}
.subscribe{width:226px;height:44px;background:var(--blue);color:#fff;font:700 13px 'Roboto',sans-serif;text-transform:uppercase;display:flex;align-items:center;justify-content:center;margin-top:14px;border-radius:3px}
.copyright{position:absolute;top:320px;left:112px;width:976px;border-top:1px solid #ddd;text-align:center;padding-top:18px;font-size:12px;color:#555}
.copyright b{color:var(--ink);font-weight:500}
</style>
</head>
<body>

<header class="section header">
  <div class="brand"><span class="brand-mark"></span><span class="brand-name">Brightlark</span></div>
  <div class="social"><span></span><span></span><span></span></div>
  <div class="phone-tab">+07 400 123 987</div>
</header>

<nav class="section nav">
  <a class="active">Home</a><a>About</a><a>Prices</a><a>Testimonials</a><a>Contact</a><a>Promotional Videos</a><a>Subject Videos</a>
</nav>

<section class="section hero" role="img" aria-label="Young pupils in green jumpers building a tall tower of blocks in a classroom">
  <div class="hero-content">
    <h1>We make awesome<br>educational videos</h1>
    <span class="btn">Play video &#9656;</span>
  </div>
</section>

<section class="section intro">
  <h2>Creating bespoke education videos to showcase<br>schools, colleges &amp; training providers<br>in the north of England</h2>
  <p class="lead">Here at Brightlark Films, we know how to create stylish, engaging, and successful educational videos for schools, colleges and training providers. We've been making them for years. We believe that when you're trying to attract new learners the best way to show how your learning establishment is better than the rest is with a compelling, top-quality video.</p>
  <div class="thumbs" style="top:380px">
    <div class="thumb" role="img" aria-label="Pupils working together at a classroom table" style="background:linear-gradient(135deg,#2f7e5c,#c9c2b0)"><svg width="40" height="40"><circle cx="20" cy="20" r="17" fill="none" stroke="#fff" stroke-width="3"/><path d="M16 12l11 8-11 8z" fill="#fff"/></svg></div>
    <div class="thumb" role="img" aria-label="Children doing a science activity with bottles" style="background:linear-gradient(135deg,#8a7560,#d6cfc2)"><svg width="40" height="40"><circle cx="20" cy="20" r="17" fill="none" stroke="#fff" stroke-width="3"/><path d="M16 12l11 8-11 8z" fill="#fff"/></svg></div>
    <div class="thumb" role="img" aria-label="Pupils making colourful crafts together" style="background:linear-gradient(135deg,#5a4a6a,#c25a4a)"><svg width="40" height="40"><circle cx="20" cy="20" r="17" fill="none" stroke="#fff" stroke-width="3"/><path d="M16 12l11 8-11 8z" fill="#fff"/></svg></div>
  </div>
</section>

<section class="section invest">
  <div class="frame-top"></div>
  <div class="photo" role="img" aria-label="Aerial drone view of a school building and car park" style="left:0;top:14px;width:644px;height:566px;background:linear-gradient(135deg,#7a756c,#4d5a42 50%,#8b8d86)"></div>
  <div class="frame-bottom"></div>
  <div class="invest-panel">
    <h2>A one-off investment<br>that brings long-term<br>results</h2>
    <span class="rule"></span>
    <p>There are so many ways to repurpose your videos and make the initial investment work for you – sharing snippets on social media, embedding the video onto your website, uploading it to your online video channel or playing it on your welcome screen in reception. The return on investment is excellent (and in some cases, instant!)</p>
    <p style="margin-top:14px"><b>BY THE WAY:</b> don't just take our word for how successful our videos are. Check out some of the wonderful feedback we've received.</p>
    <span class="btn">Read our feedback</span>
  </div>
</section>

<section class="section partners">
  <h2>Schools, colleges and training providers<br>we've worked with</h2>
  <svg class="arrow-l" width="12" height="18"><path d="M9 2L3 9l6 7" fill="none" stroke="#222" stroke-width="2"/></svg>
  <div class="logo-row">
    <div class="logo-box"><svg width="60" height="40"><rect width="60" height="40" rx="8" fill="#7cc04a"/></svg></div>
    <div class="logo-box"><svg width="56" height="56"><circle cx="28" cy="28" r="26" fill="#e08a3c"/></svg></div>
    <div class="logo-box"><svg width="40" height="40"><rect width="40" height="40" fill="#5b3a8c"/></svg></div>
    <div class="logo-box"><svg width="50" height="50"><circle cx="25" cy="25" r="23" fill="#9bb4d6"/></svg></div>
    <div class="logo-box"><svg width="80" height="32"><rect width="80" height="32" rx="6" fill="#ef8a3a"/></svg></div>
  </div>
  <div class="arrow-r"><svg width="10" height="14"><path d="M2 2l6 5-6 5" fill="none" stroke="#fff" stroke-width="2"/></svg></div>
</section>

<section class="section why">
  <h2>Why choose us</h2>
  <span class="rule"></span>
  <div class="cards">
    <div class="card">
      <div class="card-icon"><svg width="44" height="44"><circle cx="22" cy="22" r="12" fill="none" stroke="#fff" stroke-width="3"/><circle cx="22" cy="22" r="4" fill="#fff"/></svg></div>
      <h3>Experienced</h3>
      <p>We're a smart bunch of experienced video makers and we know how to create compelling videos that get results.</p>
    </div>
    <div class="card">
      <div class="card-icon alt"><svg width="46" height="40"><rect x="3" y="5" width="40" height="28" rx="3" fill="none" stroke="#fff" stroke-width="3"/><path d="M19 13l9 6-9 6z" fill="#fff"/></svg></div>
      <h3>Marketing solution</h3>
      <p>We offer a cost-effective marketing solution – no more expensive brochure designing, printing and storage hassles. A video beats traditional marketing materials hands down.</p>
    </div>
    <div class="card">
      <div class="card-icon"><svg width="40" height="44"><path d="M8 4h24M8 40h24M10 4c0 14 20 14 20 18S10 26 10 40M30 4c0 14-20 14-20 18" fill="none" stroke="#fff" stroke-width="3"/></svg></div>
      <h3>Invest time</h3>
      <p>We save you time and effort – you could invest time, effort and tech into making your own videos, but would they have the same polished, professional impact as ours?</p>
    </div>
  </div>
</section>

<section class="section custom">
  <h2>Creating customised educational videos<br>that exceed your expectations</h2>
  <p class="lead">Prefer a prospectus video over a music-driven one? No problem. In fact, we can almost always cater for your specific needs and budgets. All you have to do is ask. Our mission is to capture the heart and soul of your school, college, training company, so your potential recruits can't resist taking that next step towards enrolling. <b>Take a look at our range of video offerings,</b></p>
  <a>https://brightlarkfilms.co.uk/our-work/</a>
  <div class="thumbs" style="top:374px">
    <div class="thumb" role="img" aria-label="Two pupils in school uniform at a school entrance" style="background:linear-gradient(135deg,#4a4f7a,#b9b3a8)"><svg width="40" height="40"><circle cx="20" cy="20" r="17" fill="none" stroke="#fff" stroke-width="3"/><path d="M16 12l11 8-11 8z" fill="#fff"/></svg></div>
    <div class="thumb" role="img" aria-label="Children on a playground climbing frame" style="background:linear-gradient(180deg,#9fb2c8,#6f8a4e)"><svg width="40" height="40"><circle cx="20" cy="20" r="17" fill="none" stroke="#fff" stroke-width="3"/><path d="M16 12l11 8-11 8z" fill="#fff"/></svg></div>
    <div class="thumb" role="img" aria-label="Colourful empty classroom with tables" style="background:linear-gradient(135deg,#c8783a,#6b5a4a)"><svg width="40" height="40"><circle cx="20" cy="20" r="17" fill="none" stroke="#fff" stroke-width="3"/><path d="M16 12l11 8-11 8z" fill="#fff"/></svg></div>
  </div>
</section>

<section class="section budget">
  <div class="budget-text">
    <h2>Our videos won't eat up<br>all of your marketing<br>budget either!</h2>
    <span class="rule"></span>
    <p>You see we do things differently at Brightlark Films. Our highly experienced and dedicated team is small (but mighty) and that's how we keep costs low and affordable.</p>
    <span class="btn">View our prices</span>
  </div>
  <div class="photo" role="img" aria-label="Young child jumping out of a play tunnel" style="left:600px;top:0;width:600px;height:472px;background:radial-gradient(circle at 55% 50%,#3b4670,#6a6560 55%,#2c2a28)"></div>
</section>

<section class="section aviation">
  <h2>Licensed by the Air Safety<br>Authority</h2>
  <span class="rule"></span>
  <p>We Are Licensed Drone Operators Meaning We Can Take To The Sky.</p>
  <span class="btn">Get started</span>
</section>

<footer class="section footer">
  <div class="footer-brand"><span class="brand-mark"></span><span class="brand-name">Brightlark</span></div>
  <div class="col" style="left:352px">
    <h4>Navigation</h4>
    <ul><li>Home</li><li>About</li><li>Prices</li><li>Testimonials</li><li>Contact</li><li>Promotional Videos</li><li>Subject Videos</li></ul>
  </div>
  <div class="col" style="left:534px">
    <h4>Contact us</h4>
    <div class="contact-item"><svg width="12" height="16"><path d="M6 1a5 5 0 0 1 5 5c0 4-5 9-5 9S1 10 1 6a5 5 0 0 1 5-5z" fill="var(--blue)"/><circle cx="6" cy="6" r="2" fill="#fff"/></svg><span>Studio 4, Larkfield Business Park,<br>Hexham, Northumberland. NE46 2XY.</span></div>
    <div class="contact-item"><svg width="12" height="16"><path d="M2 2l3-1 2 4-2 1c1 3 2 4 4 5l1-2 4 2-1 3C8 14 1 8 2 2z" fill="var(--blue)"/></svg><span>07400 123 987</span></div>
    <div class="contact-item"><svg width="14" height="16"><rect x="1" y="3" width="12" height="9" fill="var(--blue)"/><path d="M1 3l6 5 6-5" fill="none" stroke="#fff" stroke-width="1.2"/></svg><span>info@brightlarkfilms.co.uk</span></div>
  </div>
  <div class="col" style="left:862px">
    <h4>Newsletter</h4>
    <div class="email-field">Your Email</div>
    <div class="subscribe">Subscribe</div>
  </div>
  <div class="copyright">Copyright © 2023 <b>BRIGHTLARK FILMS</b> - All Rights Reserved.</div>
</footer>

</body>
</html>
```